TALLYMORA (www.tallymora.com.zz) needs exciting professional Business Cards

TALLYMORA is an exciting new start-up targeting innovative ways to engage with retail customers at the point of sale.
Our Vision
Through applying new thinking to an old business we are reinventing selected segments of the Australian retail messaging industry, generating significant value for our customers, our suppliers, and our owners.
We operate with integrity, agility, and intelligence to doing things smarter, faster and more efficiently.
We bring deep industry expertise, deep relationships with customers and suppliers, and a will to see the old ways give way to smarter ways – this is why we win.
From this economically sustainable platform, we will examine the disruption of other market segments by further leveraging the elements that make us successful.
Our Values
With our clients, with our suppliers, with our staff, and with our owners:
# We Partner – We align the interest of all stakeholders by striving to ensure everything we do is mutually beneficial and commercially sustainable in the long term. We are clear with all our stakeholders about what our expectations are of them, and we seek clarity from them in their expectations of us.
# We Innovate – In the segments we choose to compete in, we bring fresh ideas, new business processes, the right relationships, and the right technology to ensure the supply chain is nimble, competitive, and reliable.
# We are Accountable – We say what we will do, and then do what we say.
# We Perform – We use our skills, relationships, and reputation to deliver value to our customers, suppliers, and owners.
Initially we are building our business from low-tech through printing promotional offers and retailer messages on ATM and EFTPOS receipts, but as soon as cash flow supports it we will be engaging in high-tech real-time targeted offers to the specific consumer.
I'd like the cards to reflect our values.
Please check out the web site we have just launched - it is pretty basic but it has only been up a week. We intend to sharpen it over the coming weeks, but you'll get the idea of what our core messages are.
I have recently sourced a logo from SketchHive, and have attached the source files for use.
Personal information to include:
Name: FirstName Surname
Title: Managing Director
email: first.surname@tallymora.com.zz
Mobile: +61-472-555-318
Generic Co Details to include:
Web: www.tallymora.com.zz
email: tallymora@tallymora.com.zz
Fax: +61-8-5037-2164
Offices & Agents: Sydney, Melbourne, Brisbane, Adelaide, Perth
Byline: Innovation . Integrity . Service
Target Market(s)
Our customers are large corporations that have professional Point Of Sale marketing experts looking for a supplier with an edge over others in a crowded market. The buyer of our product and services is ultimately a communications expert.
They want to see distinctive competence, and an agility of thinking that will make them money through driving more consumer spending.
Industry/Entity Type
Retail
Look and feel
Each slider illustrates characteristics of the customer's brand and the style your logo design should communicate.

```html
<!DOCTYPE html>
<html lang="en">
<head>
<meta charset="utf-8">
<title>TALLYMORA Business Cards</title>
<link rel="stylesheet" href="https://fonts.googleapis.com/css2?family=Open+Sans:ital,wght@0,400;0,600;0,700;1,600&display=swap">
<style>
  :root {
    --stage: #b9b9b9;
    --card-black: #0b0b0b;
    --card-white: #ffffff;
    --brand-blue: #0a7fcb;
    --ink: #111111;
    --ink-light: #f2f2f2;
    --ring: #2c2c2c;
  }
  * { box-sizing: border-box; margin: 0; padding: 0; }
  html, body {
    width: 1200px; height: 900px; overflow: hidden;
    background: var(--stage);
    font-family: "Open Sans", Arial, sans-serif;
  }
  .stage {
    width: 1200px; height: 900px;
    display: flex; align-items: center; justify-content: center; gap: 40px;
  }
  .card {
    width: 540px; height: 320px; position: relative; overflow: hidden;
    box-shadow: 0 6px 18px rgba(0,0,0,.25);
  }

  /* Back */
  .card-back {
    background: var(--card-black);
    display: flex; align-items: center; justify-content: center; gap: 22px;
  }
  .card-back .mark-dot {
    width: 44px; height: 44px; border-radius: 50%;
    background: var(--ring);
  }
  .card-back .wordmark {
    font-size: 54px; font-weight: 700; color: var(--brand-blue);
    letter-spacing: -1px; line-height: 1;
  }

  /* Front */
  .card-front { background: var(--card-white); display: flex; flex-direction: column; }
  .front-top { position: relative; height: 186px; flex: none; }
  .front-top .wordmark {
    position: absolute; left: 22px; top: 20px;
    font-size: 44px; font-weight: 700; color: var(--brand-blue);
    letter-spacing: -1px; line-height: 1;
  }
  .person {
    position: absolute; right: 24px; top: 92px; text-align: right; color: var(--ink);
  }
  .person .name {
    font-size: 17px; font-weight: 700; color: var(--brand-blue);
    letter-spacing: 1px; line-height: 1.3;
  }
  .person .title { font-size: 11.5px; line-height: 1.4; margin-bottom: 8px; }
  .person .line { font-size: 11.5px; line-height: 1.45; }

  .front-band {
    flex: 1; background: var(--card-black); color: var(--ink-light);
    padding: 10px 22px; font-size: 11.5px; line-height: 1.45;
  }
  .front-band .company { color: var(--brand-blue); font-weight: 600; font-style: italic; font-size: 12.5px; }
  .front-band .label { color: var(--brand-blue); font-weight: 600; font-style: italic; }
</style>
</head>
<body>
<main class="stage">
  <section class="card card-back" aria-label="Business card back">
    <span class="mark-dot"></span>
    <span class="wordmark">TALLYMORA</span>
  </section>

  <section class="card card-front" aria-label="Business card front">
    <div class="front-top">
      <div class="wordmark">TALLYMORA</div>
      <div class="person">
        <p class="name">DANIEL REEVE</p>
        <p class="title">Managing Director</p>
        <p class="line">+61-472-555-318</p>
        <p class="line">first.surname@tallymora.com.zz</p>
      </div>
    </div>
    <div class="front-band">
      <p class="company">TALLYMORA Pty Ltd</p>
      <p><span class="label">Web:</span> www.tallymora.com.zz</p>
      <p><span class="label">Email:</span> tallymora@tallymora.com.zz</p>
      <p><span class="label">Fax:</span> +61-8-5037-2164</p>
      <p><span class="label">Offices &amp; Agents:</span> Sydney, Melbourne, Brisbane, Adelaide, Perth</p>
      <p><span class="label">Byline:</span> Innovation . Integrity . Service</p>
    </div>
  </section>
</main>
</body>
</html>
```